Full page ad in a magazine

We would like an ad designed to be placed for advertising in magazines, theater playbills, etc. I have attached a copy of some previous ads that were done for us, although they need much improvement and redesigned. We have won "best chiropractor" awards that can be seen on our website home page at ferncliffspineandjoint.com

```html
<!DOCTYPE html>
<html lang="en">
<head>
<meta charset="utf-8">
<title>Ferncliff Spine &amp; Joint Center – Magazine Ad</title>
<link rel="stylesheet" href="https://fonts.googleapis.com/css2?family=Merriweather:ital,wght@0,400;0,700;1,400;1,900&family=Questrial&family=Archivo:wght@700&display=swap">
<style>
  :root {
    --brand-red: #8a1a1c;
    --ink: #2e2e2e;
    --tab-gray: #3d3d3d;
    --line-gray: #b5b5b5;
    --stage: #ffffff;
    --white: #ffffff;
  }
  html, body {
    margin: 0;
    width: 1141px;
    height: 1200px;
    overflow: hidden;
    background: var(--stage);
  }
  .ad {
    position: absolute;
    left: 8px;
    top: 0;
    width: 1150px;
    height: 1228px;
    transform: scale(0.977);
    transform-origin: 0 0;
    overflow: hidden;
    background: var(--white);
    font-family: "Merriweather", serif;
  }
  .hero-photo {
    position: absolute;
    left: 0; top: 0;
    width: 1150px; height: 957px;
    background: linear-gradient(180deg, #f4f4f4 0%, #e6e6e6 45%, #8d8d8d 62%, #4a4a4a 78%, #2f2f2f 100%);
  }
  .brand {
    position: absolute;
    left: 600px; top: 52px;
    display: flex; align-items: center; gap: 16px;
  }
  .brand-mark {
    width: 86px; height: 86px;
    background: #a9a9a9;
  }
  .brand-name {
    font-weight: 700;
    font-size: 34px;
    line-height: 1.2;
    color: var(--brand-red);
    letter-spacing: 1px;
  }
  .headline { position: absolute; left: 70px; top: 188px; color: var(--brand-red); }
  .headline .lead {
    display: block; margin-left: 16px;
    font-style: italic; font-weight: 400; font-size: 48px; color: var(--ink);
  }
  .headline .big {
    display: block;
    font-style: italic; font-weight: 900; font-size: 112px; line-height: 106px;
    letter-spacing: -1px;
  }
  .headline .tail {
    display: block; margin-left: 86px; margin-top: -4px;
    font-style: italic; font-weight: 400; font-size: 58px; color: var(--ink);
  }
  .services-pill {
    position: absolute; left: 66px; top: 612px;
    width: 452px; height: 44px; border-radius: 22px;
    background: var(--brand-red); color: var(--white);
    font-size: 28px; line-height: 44px; text-align: center;
  }
  .conditions {
    position: absolute; left: 72px; top: 683px;
    display: grid; grid-template-columns: 265px 220px; row-gap: 6px;
    margin: 0; padding: 0; list-style: none;
  }
  .conditions li {
    font-size: 28px; line-height: 38px; color: var(--white);
    display: flex; align-items: center; gap: 14px;
  }
  .conditions li::before {
    content: ""; width: 10px; height: 10px; border-radius: 50%;
    background: var(--brand-red); box-shadow: 0 0 0 3px #ddd;
  }
  .insurance-note {
    position: absolute; right: 52px; top: 904px;
    font-style: italic; font-size: 24px; color: var(--white);
  }
  .doctor-photo {
    position: absolute; left: 40px; top: 885px;
    width: 246px; height: 246px; border-radius: 50%;
    border: 8px solid var(--white);
    background: radial-gradient(circle at 50% 40%, #7a6a5e 0%, #4a4747 55%, #2a2a2c 100%);
  }
  .name-tab {
    position: absolute; left: 313px; top: 957px;
    height: 40px; padding: 0 16px;
    background: var(--tab-gray); color: var(--white);
    border-radius: 0 0 6px 6px;
    font-family: "Questrial", sans-serif; font-size: 27px; line-height: 40px;
  }
  .phone {
    position: absolute; left: 310px; top: 1010px;
    display: flex; align-items: center; gap: 12px;
    font-family: "Archivo", sans-serif; font-weight: 700; font-size: 48px; color: #333;
  }
  .address {
    position: absolute; left: 313px; top: 1066px;
    font-family: "Questrial", sans-serif; font-size: 26px; line-height: 32px; color: #333;
  }
  .awards {
    position: absolute; left: 735px; top: 996px;
    width: 360px; height: 126px;
    border: 2px solid var(--line-gray); box-sizing: border-box;
  }
  .awards-label {
    position: absolute; left: 50%; top: -13px; transform: translateX(-50%);
    background: var(--white); padding: 0 10px;
    font-family: "Questrial", sans-serif; font-size: 17px; color: #666; white-space: nowrap;
  }
  .badge-seal { position: absolute; left: 14px; top: 20px; width: 90px; height: 90px; border-radius: 50%; background: #1e1e1e; box-shadow: 0 0 0 4px #e8b923; }
  .badge-card { position: absolute; top: 18px; width: 108px; height: 92px; background: #3b4fa0; }
  .badge-card.one { left: 118px; }
  .badge-card.two { left: 238px; }
  .web-bar {
    position: absolute; left: 0; top: 1157px;
    width: 1150px; height: 71px;
    background: var(--brand-red); color: var(--white);
    text-align: center; font-size: 44px; line-height: 71px;
  }
  .web-bar b { font-weight: 700; }
</style>
</head>
<body>
<main class="ad">
  <div class="hero-photo" role="img" aria-label="Black and white photo of a mountain biker with a red backpack overlooking a forested valley"></div>

  <div class="brand">
    <span class="brand-mark"></span>
    <span class="brand-name">FERNCLIFF<br>SPINE &amp; JOINT CENTER</span>
  </div>

  <h1 class="headline" style="margin:0;font-weight:400">
    <span class="lead">We’ll get you</span>
    <span class="big">Back</span>
    <span class="big">to the life</span>
    <span class="tail">you enjoy!</span>
  </h1>

  <div class="services-pill">CHIROPRACTIC • MASSAGE</div>

  <ul class="conditions">
    <li>Back Pain</li><li>Joint Pain</li>
    <li>Neck Pain</li><li>Sciatica</li>
    <li>Headaches</li><li>Fatigue</li>
  </ul>

  <p class="insurance-note" style="margin:0">Medicare and most Insurance accepted.</p>

  <div class="doctor-photo" role="img" aria-label="Portrait photo of the chiropractor in a suit"></div>
  <div class="name-tab">Marcus Hale, DC</div>

  <div class="phone">
    <svg width="44" height="44" viewBox="0 0 44 44" aria-hidden="true">
      <circle cx="22" cy="22" r="22" fill="#8a1a1c"/>
      <path d="M15 11c2 0 3 4 4 6 0 1-2 2-2 3 1 3 4 6 7 7 1 0 2-2 3-2 2 1 6 2 6 4 0 2-3 4-5 4-9 0-17-8-17-17 0-2 2-5 4-5z" fill="#fff"/>
    </svg>
    757-555-0148
  </div>
  <div class="address">2150 Alder Mill Rd., #310<br>Ferncliff, VA 23190</div>

  <div class="awards">
    <span class="awards-label">Best Chiropractor</span>
    <span class="badge-seal"></span>
    <span class="badge-card one"></span>
    <span class="badge-card two"></span>
  </div>

  <div class="web-bar">www.<b>ferncliffspineandjoint</b>.com</div>
</main>
</body>
</html>
```